Marrowfield Biomedical Research Institute (MBRX) Web Design

MBRX is a non-profit organization focused on saving the lives of terminally ill patients by becoming the leaders in cutting-edge research, innovative technologies, utilizing national and international partnerships as well as the associated allopathic and naturopathic treatments necessary to do so.

Our primary focus is raising funds to support the research and acquisition of new technologies for life saving treatments which are NOT a one size fits all approach like conventional medicine but rather a marriage of the latest technologies used in combination with other new treatment possibilities for a successful end result.

Our domain is marrowfieldbrx.org

Logo files are attached.

Looking for something clean, light, healthy.

Target Market(s)

The site should look and feel towards research/scientific grant writing.
Medical professionals, Medical Scientists.

Industry/Entity Type

Medical And Science

Number of Pages Required

4 page

Requirements
Nice to have
• Here are examples of sites I like in the order of how much I like them.
• https://www.palvenhope.org/give.html
• https://www.thekqtf.org/donate-to-kqtf
• https://www.velmorecure.org/we-are-vci/join-the-cause
• https://www.tumarex.org/involved/donate.html
• https://give.dwkt.org/checkout/donation?eid=58217
• https://www.quillavent.org/how-you-can-help
• https://donate3.tumarex.org/

```html
<!DOCTYPE html>
<html lang="en">
<head>
<meta charset="utf-8">
<title>Marrowfield Biomedical Research Institute</title>
<link href="https://fonts.googleapis.com/css2?family=Open+Sans:wght@400;600;700&family=Roboto:wght@400;500&display=swap" rel="stylesheet">
<style>
:root{
  --green:#5aa63a;
  --blue:#1f72b8;
  --blue-dark:#135c9e;
  --ink:#222;
  --text:#555;
  --nav:#444;
  --grey-band:#f2f2f2;
  --footer:#0b0b0b;
  --white:#fff;
}
*{box-sizing:border-box;margin:0;padding:0}
html,body{width:1200px;height:3136px;overflow:hidden;background:var(--white)}
body{position:relative;font-family:'Open Sans',sans-serif;color:var(--text)}
.abs{position:absolute}
h1,h2,h3{font-family:'Roboto',sans-serif;font-weight:400;color:var(--ink)}

/* header */
.site-header{left:0;top:0;width:1200px;height:140px;background:var(--white)}
.brand{left:88px;top:30px;display:flex;align-items:center;gap:14px}
.brand-mark{width:60px;height:60px;border-radius:50%;background:var(--green)}
.brand-name{font-weight:700;color:var(--green);font-size:34px;line-height:1}
.brand-sub{font-weight:700;color:var(--green);font-size:10.5px;letter-spacing:.5px;margin-top:4px}
.contact-bar{right:88px;top:28px;display:flex;align-items:center;gap:28px;font-family:'Roboto',sans-serif;font-size:18px;color:var(--nav)}
.contact-item{display:flex;align-items:center;gap:10px}
.contact-icon{width:34px;height:34px;border-radius:50%;border:2px solid var(--green);display:flex;align-items:center;justify-content:center}
.donate-btn{border:2px solid var(--blue);border-radius:18px;color:var(--blue);padding:4px 16px;font-size:16px}
.main-nav{right:88px;top:80px;display:flex;gap:34px;font-family:'Roboto',sans-serif;font-size:18px;color:var(--nav)}
.main-nav .active{color:var(--blue)}

/* hero */
.hero{left:0;top:140px;width:1200px;height:630px;overflow:hidden}
.hero-photo{left:0;top:0;width:1200px;height:630px;
  background:
    radial-gradient(ellipse 120px 70px at 720px 560px,rgba(255,190,90,.95),rgba(255,160,60,0) 100%),
    radial-gradient(ellipse 260px 180px at 830px 130px,#f4f7fb,rgba(244,247,251,0) 100%),
    radial-gradient(ellipse 220px 160px at 780px 360px,#1d2736,rgba(29,39,54,0) 100%),
    radial-gradient(ellipse 180px 260px at 1120px 420px,#2a3446,rgba(42,52,70,0) 100%),
    radial-gradient(ellipse 260px 200px at 300px 120px,#c9d7ea,rgba(201,215,234,0) 100%),
    linear-gradient(110deg,#eaf0f7 0%,#dbe4ef 30%,#9fb3cb 52%,#5d7290 68%,#c3d0df 85%,#8c9db3 100%)}
.hero-curve{left:0;top:0}
.hero-title{left:90px;top:192px;width:352px;height:184px;background:rgba(255,255,255,.84);padding:20px 24px}
.hero-title .l1{font-family:'Roboto',sans-serif;font-size:50px;line-height:54px;color:var(--green)}
.hero-title .l2{font-family:'Roboto',sans-serif;font-size:50px;line-height:54px;color:var(--blue)}
.hero-title .l3{font-family:'Roboto',sans-serif;font-size:24px;letter-spacing:2px;color:#333;margin-top:4px}
.slider-arrows{left:88px;top:450px;display:flex;gap:4px}
.slider-arrows span{width:24px;height:24px;border-radius:50%;background:#666;display:flex;align-items:center;justify-content:center}

/* welcome */
.welcome-frame{left:94px;top:861px;width:314px;height:303px;background:var(--green)}
.welcome-photo{left:119px;top:886px;width:314px;height:303px;box-shadow:0 10px 18px rgba(0,0,0,.25);
  background:
    radial-gradient(ellipse 90px 150px at 150px 190px,#f6f8fa,rgba(246,248,250,0) 100%),
    radial-gradient(ellipse 60px 50px at 170px 230px,#1f5f8f,rgba(31,95,143,0) 100%),
    radial-gradient(ellipse 50px 55px at 150px 70px,#4a3a32,rgba(74,58,50,0) 100%),
    linear-gradient(135deg,#e8edf1 0%,#cdd6de 45%,#9eabb8 100%)}
.welcome-text{left:472px;top:895px;width:640px}
.welcome-text h2{font-size:33px}
.welcome-text h3{font-size:21px;margin-top:8px;font-weight:500}
.body-copy{font-size:13.5px;line-height:24px;text-align:justify;margin-top:12px;color:var(--text)}
.btn-green{display:inline-block;background:var(--green);color:var(--white);border-radius:18px;font-size:14px;padding:7px 16px;margin-top:20px}

/* what we do */
.services{left:0;top:1271px;width:1200px;height:572px;
  background:
    radial-gradient(ellipse 260px 300px at 1060px 330px,rgba(120,180,225,.35),rgba(120,180,225,0) 100%),
    radial-gradient(ellipse 300px 200px at 150px 80px,rgba(90,160,215,.35),rgba(90,160,215,0) 100%),
    linear-gradient(120deg,#2a84c9 0%,var(--blue) 45%,var(--blue-dark) 100%)}
.services h2{position:absolute;left:0;width:1200px;top:66px;text-align:center;color:var(--white);font-size:33px}
.service-card{top:154px;width:293px;height:308px;background:var(--white);text-align:center}
.service-img{height:171px}
.service-card h3{font-size:19px;margin-top:16px}
.service-card p{font-size:12px;line-height:18px;color:#777;margin:6px 24px 0}
.btn-small{display:inline-block;background:var(--green);color:var(--white);border-radius:12px;font-size:11px;padding:2px 16px;margin-top:8px}

/* care */
.care-text{left:160px;top:1965px;width:535px}
.care-text h2{font-size:33px}
.care-photo{left:727px;top:1937px;width:306px;height:306px;border-radius:50%;border:2px solid #333;padding:8px}
.care-photo div{width:100%;height:100%;border-radius:50%;
  background:
    radial-gradient(ellipse 70px 40px at 170px 180px,#7fe0ff,rgba(127,224,255,0) 100%),
    radial-gradient(ellipse 120px 90px at 90px 60px,#e6eef4,rgba(230,238,244,0) 100%),
    radial-gradient(ellipse 100px 120px at 210px 80px,#1c3552,rgba(28,53,82,0) 100%),
    linear-gradient(160deg,#b9cfe0 0%,#4f8fbd 55%,#9fc3dc 100%)}

/* blog */
.blog{left:0;top:2322px;width:1200px;height:408px;background:var(--grey-band)}
.blog h2{position:absolute;left:0;width:1200px;top:68px;text-align:center;font-size:33px}
.blog-card{top:157px;width:497px;height:186px;background:var(--white);box-shadow:0 3px 8px rgba(0,0,0,.12);display:flex}
.blog-img{width:162px;height:186px;flex:none}
.blog-body{padding:22px 24px 0 24px}
.blog-body h3{font-size:17px;color:#333}
.blog-date{font-size:13px;color:#555;margin-top:4px}
.blog-body p{font-size:13px;line-height:18px;text-align:justify;margin-top:2px}
.blog-more{font-size:13px;color:var(--green);margin-top:4px}

/* footer */
.site-footer{left:0;top:2730px;width:1200px;height:406px;background:var(--footer);color:#ddd}
.newsletter{left:278px;top:50px;display:flex;align-items:center;gap:28px}
.newsletter h2{color:var(--white);font-size:27px;letter-spacing:1px}
.newsletter-form{display:flex;width:444px;height:42px;border-radius:21px;overflow:hidden;background:var(--white)}
.newsletter-form .field{flex:1;font-size:12px;color:#999;padding:12px 14px}
.newsletter-form .submit{background:var(--green);color:var(--white);font-size:12px;width:100px;display:flex;align-items:center;justify-content:center}
.footer-rule{left:90px;width:1020px;height:1px;background:#333}
.footer-col{top:170px;font-size:12.5px;line-height:24px;color:#ddd}
.footer-col h4{font-weight:400;font-size:14px;color:var(--white);margin-bottom:4px}
.social{display:flex;gap:10px;margin-top:6px}
.social span{width:30px;height:30px;border-radius:50%;border:2px solid var(--white);display:flex;align-items:center;justify-content:center}
.social span i{width:12px;height:12px;border-radius:50%;background:var(--white)}
.copyright{left:0;width:1200px;top:354px;text-align:center;font-size:11px;color:#ddd}
</style>
</head>
<body>

<header class="site-header abs">
  <div class="brand abs">
    <div class="brand-mark"></div>
    <div>
      <div class="brand-name">MBRX</div>
      <div class="brand-sub">MARROWFIELD BIOMEDICAL RESEARCH INSTITUTE</div>
    </div>
  </div>
  <div class="contact-bar abs">
    <div class="contact-item">
      <span class="contact-icon"><svg width="16" height="16" viewBox="0 0 24 24"><path fill="#5aa63a" d="M6.6 10.8a15 15 0 0 0 6.6 6.6l2.2-2.2c.3-.3.7-.4 1-.2 1.1.4 2.3.6 3.6.6.6 0 1 .4 1 1V20c0 .6-.4 1-1 1A17 17 0 0 1 3 4c0-.6.4-1 1-1h3.5c.6 0 1 .4 1 1 0 1.3.2 2.5.6 3.6.1.3 0 .7-.2 1z"/></svg></span>
      450.555.0192
    </div>
    <div class="contact-item">
      <span class="contact-icon"><svg width="16" height="16" viewBox="0 0 24 24"><path fill="#5aa63a" d="M3 5h18v14H3z"/><path fill="none" stroke="#fff" stroke-width="2" d="M3 6l9 7 9-7"/></svg></span>
      info@marrowfieldbrx.org
    </div>
    <span class="donate-btn">Donate</span>
  </div>
  <nav class="main-nav abs">
    <span class="active">Home</span><span>About us</span><span>Research</span><span>Care &amp; Treatment</span><span>Training</span><span>Contact</span>
  </nav>
</header>

<section class="hero abs">
  <div class="hero-photo abs" role="img" aria-label="Gloved hands adjusting a laboratory microscope under warm light"></div>
  <svg class="hero-curve abs" width="1200" height="630" viewBox="0 0 1200 630">
    <defs>
      <linearGradient id="curveLine" x1="0" x2="1">
        <stop offset="0" stop-color="#9a9a9a"/><stop offset=".5" stop-color="#c8c8c8"/><stop offset="1" stop-color="#9a9a9a"/>
      </linearGradient>
    </defs>
    <path d="M0 548 Q600 690 1200 540 L1200 630 L0 630 Z" fill="#fff"/>
    <path d="M0 552 Q600 700 1200 544" fill="none" stroke="url(#curveLine)" stroke-width="9"/>
  </svg>
  <div class="hero-title abs">
    <div class="l1">Marrowfield</div>
    <div class="l2">Biomedical</div>
    <div class="l3">Research Institute</div>
  </div>
  <div class="slider-arrows abs">
    <span><svg width="10" height="10" viewBox="0 0 10 10"><path d="M6.5 1.5 3 5l3.5 3.5" fill="none" stroke="#fff" stroke-width="1.6"/></svg></span>
    <span><svg width="10" height="10" viewBox="0 0 10 10"><path d="M3.5 1.5 7 5 3.5 8.5" fill="none" stroke="#fff" stroke-width="1.6"/></svg></span>
  </div>
</section>

<section>
  <div class="welcome-frame abs"></div>
  <div class="welcome-photo abs" role="img" aria-label="Scientist in a lab coat reading a tablet in a laboratory"></div>
  <div class="welcome-text abs">
    <h2>Welcome to Marrowfield Biomedical</h2>
    <h3>Neque porro quisquam est qui dolorem ipsum</h3>
    <p class="body-copy">It is a long established fact that a reader will be distracted by the readable content of a page when looking at its layout. The point of using Lorem Ipsum is that it has a more-or-less normal distribution of letters, as opposed to using 'Content here, content here', making it look like readable English. Many desktop publishing packages and web page editors now use Lorem Ipsum as their default model text, and a search for 'lorem ipsum' will uncover many</p>
    <span class="btn-green">Read More &raquo;</span>
  </div>
</section>

<section class="services abs">
  <h2>What We Do</h2>
  <div class="service-card abs" style="left:125px">
    <div class="service-img" role="img" aria-label="Two researchers working at a lab bench" style="background:radial-gradient(ellipse 60px 70px at 90px 100px,#fafbfc,rgba(250,251,252,0) 100%),radial-gradient(ellipse 60px 70px at 190px 90px,#f3f5f7,rgba(243,245,247,0) 100%),radial-gradient(ellipse 70px 50px at 250px 140px,#2d3a4a,rgba(45,58,74,0) 100%),linear-gradient(135deg,#e4e9ee,#b4c1ce 60%,#7d8ea2)"></div>
    <h3>Cutting-edge research</h3>
    <p>It has survived not only five centuries, but also the leap into electronic</p>
    <span class="btn-small">View More</span>
  </div>
  <div class="service-card abs" style="left:447px">
    <div class="service-img" role="img" aria-label="Blue-lit laboratory glassware and test tubes" style="background:radial-gradient(ellipse 80px 60px at 90px 60px,#eaf6fd,rgba(234,246,253,0) 100%),radial-gradient(ellipse 90px 70px at 200px 130px,#0f5a92,rgba(15,90,146,0) 100%),linear-gradient(135deg,#cfe7f6,#6fb2de 55%,#2a7db8)"></div>
    <h3>Innovative technologies</h3>
    <p>It has survived not only five centuries, but also the leap into electronic</p>
    <span class="btn-small">View More</span>
  </div>
  <div class="service-card abs" style="left:767px">
    <div class="service-img" role="img" aria-label="Open hands holding green leaves and a small remedy bottle" style="background:radial-gradient(ellipse 50px 45px at 200px 95px,#5f8f3a,rgba(95,143,58,0) 100%),radial-gradient(ellipse 110px 60px at 140px 120px,#e7c9b4,rgba(231,201,180,0) 100%),linear-gradient(135deg,#f6f4f0,#e6e1d8 60%,#cfc6b6)"></div>
    <h3>Naturopathic treatments</h3>
    <p>It has survived not only five centuries, but also the leap into electronic</p>
    <span class="btn-small">View More</span>
  </div>
</section>

<section>
  <div class="care-text abs">
    <h2>Care &amp; Treatment</h2>
    <p class="body-copy">It is a long established fact that a reader will be distracted by the readable content of a page when looking at its layout. The point of using Lorem Ipsum is that it has a more-or-less normal distribution of letters, as opposed to using 'Content here, content here', making it look like readable English. Many desktop publishing packages and web page editors now use Lorem Ipsum as their default .</p>
    <span class="btn-green">Read More &raquo;</span>
  </div>
  <div class="care-photo abs"><div role="img" aria-label="Microscope with a digital data overlay in blue light"></div></div>
</section>

<section class="blog abs">
  <h2>Latest Blog</h2>
  <article class="blog-card abs" style="left:88px">
    <div class="blog-img" role="img" aria-label="Gloved hand placing a sample under a microscope" style="background:radial-gradient(ellipse 50px 40px at 100px 150px,#2b7fd0,rgba(43,127,208,0) 100%),radial-gradient(ellipse 60px 70px at 70px 50px,#f1f3f5,rgba(241,243,245,0) 100%),linear-gradient(135deg,#d9e1e8,#8fa2b5 55%,#3f5d7d)"></div>
    <div class="blog-body">
      <h3>Nemo Enim Ipsam Volup</h3>
      <div class="blog-date">09-07-2017</div>
      <p>Lorem Ipsum has been the industry's standard dummy text ever since the 1500s, when an unknown printer took a galley</p>
      <div class="blog-more">Read More &gt;&gt;</div>
    </div>
  </article>
  <article class="blog-card abs" style="left:612px">
    <div class="blog-img" role="img" aria-label="Two researchers examining a sample in a lab" style="background:radial-gradient(ellipse 40px 50px at 55px 70px,#c9703e,rgba(201,112,62,0) 100%),radial-gradient(ellipse 60px 80px at 110px 110px,#f4f6f8,rgba(244,246,248,0) 100%),linear-gradient(135deg,#e9edf1,#b3c1ce 55%,#6b7d90)"></div>
    <div class="blog-body">
      <h3>Nemo Enim Ipsam Volup</h3>
      <div class="blog-date">09-07-2017</div>
      <p>Lorem Ipsum has been the industry's standard dummy text ever since the 1500s, when an unknown printer took a galley</p>
      <div class="blog-more">Read More &gt;&gt;</div>
    </div>
  </article>
</section>

<footer class="site-footer abs">
  <div class="newsletter abs">
    <h2>NEWSLETTER</h2>
    <div class="newsletter-form"><span class="field">email@example.com</span><span class="submit">SUBSCRIBE</span></div>
  </div>
  <div class="footer-rule abs" style="top:138px"></div>
  <div class="footer-col abs" style="left:96px">
    <h4>INFORMATION</h4>
    <div>&raquo; Privacy Policy</div><div>&raquo; Organisation</div><div>&raquo; Utilising national</div><div>&raquo; Contact Us</div>
  </div>
  <div class="footer-col abs" style="left:370px">
    <h4>LINKS</h4>
    <div>&raquo; Training</div><div>&raquo; Research</div><div>&raquo; Care &amp; Treatment</div><div>&raquo; About us</div>
  </div>
  <div class="footer-col abs" style="left:614px">
    <h4>CONTACT US</h4>
    <div>Address : Veldenstraat 12B 4812 KM</div><div>&nbsp;Dorrendam Nederland</div><div>Phone : +31 (0)150-555012</div><div>Email : info@marrowfieldbrx.org</div>
  </div>
  <div class="footer-col abs" style="left:938px;top:164px">
    <h4>FOLLOW US OUT THERE</h4>
    <div class="social"><span><i></i></span><span><i></i></span><span><i></i></span></div>
  </div>
  <div class="footer-rule abs" style="top:330px"></div>
  <div class="copyright abs">Copyright &copy; 2017. All Rights Reserved</div>
</footer>

</body>
</html>
```